Bright Fern Painting needs a new business card. See attachments for our logo and current card as an example.
We want to utilize the same colors in the logo, and keep all the information that is currently on it. Just need an updated and modern design.
We are open to loosing the Association Logos if it means a better design.
We are also entertaining a spot for a picture of a headshot of the person listed on the card. Head shot can be finished later.

```html
<!DOCTYPE html>
<html lang="en">
<head>
<meta charset="utf-8">
<title>Bright Fern Painting – Business Card</title>
<link href="https://fonts.googleapis.com/css2?family=Jost:wght@400;500&family=Roboto:wght@400;500;700&display=swap" rel="stylesheet">
<style>
  :root {
    --backdrop: #2a2a2a;
    --maroon: #6b3a35;
    --fern: #3d4a2e;
    --paper: #ffffff;
    --ink: #3a3a3a;
    --brush-tone: #f2eeec;
  }
  * { box-sizing: border-box; margin: 0; padding: 0; }
  html, body {
    width: 1200px; height: 801px; overflow: hidden;
    background: var(--backdrop);
  }
  .stage {
    width: 1200px; height: 801px;
    display: flex; align-items: center; justify-content: center; gap: 40px;
  }
  .card {
    position: relative; width: 540px; height: 309px; overflow: hidden;
  }

  /* Front */
  .card-front { background: var(--maroon); }
  .front-brand {
    position: absolute; right: 34px; top: 34px;
    font-family: "Jost", sans-serif; font-weight: 500;
    color: var(--paper); font-size: 40px; line-height: 1.05;
    text-align: right; text-transform: uppercase;
  }
  .paint-stroke {
    position: absolute; left: 250px; right: 0; top: 168px; height: 104px;
    background: var(--paper);
  }
  .brush-art {
    position: absolute; left: 22px; top: 150px; width: 250px; height: 130px;
    background: var(--brush-tone); border-radius: 6px;
  }
  .service-list {
    position: absolute; right: 30px; top: 178px; list-style: none;
    font-family: "Jost", sans-serif; font-size: 15px; line-height: 1.3;
    color: var(--ink); text-align: right;
  }
  .service-list li::after {
    content: ""; display: inline-block; width: 6px; height: 6px;
    border-radius: 50%; background: var(--ink);
    margin-left: 8px; vertical-align: middle;
  }

  /* Back */
  .card-back { background: var(--paper); }
  .back-brand {
    position: absolute; left: 40px; top: 78px;
    display: flex; align-items: center; gap: 10px;
    font-family: "Jost", sans-serif; font-weight: 500;
    color: var(--fern); font-size: 30px; line-height: 1.05; text-transform: uppercase;
  }
  .brand-square { width: 14px; height: 14px; background: var(--fern); flex: none; }
  .contact {
    position: absolute; left: 260px; top: 92px;
    font-family: "Roboto", sans-serif;
  }
  .person-name { color: var(--fern); font-weight: 700; font-size: 24px; letter-spacing: .5px; }
  .person-role { color: var(--maroon); font-weight: 500; font-size: 15px; letter-spacing: .5px; margin-bottom: 14px; }
  .contact-line {
    display: flex; align-items: center; gap: 8px;
    color: var(--ink); font-size: 15px; margin-top: 4px;
  }
  .contact-line svg { width: 14px; height: 14px; fill: var(--fern); flex: none; }
  .web-band {
    position: absolute; left: 0; right: 0; bottom: 34px; height: 34px;
    background: var(--fern); display: flex; align-items: center;
    padding-left: 56px;
    font-family: "Roboto", sans-serif; font-size: 14px;
    color: var(--paper); letter-spacing: 5px;
  }
  .band-brush {
    position: absolute; right: 26px; bottom: 30px; width: 52px; height: 42px;
    background: var(--maroon); border-radius: 3px;
  }
</style>
</head>
<body>
  <main class="stage">
    <section class="card card-front">
      <div class="paint-stroke"></div>
      <div class="brush-art" role="img" aria-label="Illustration of a large paintbrush laying a white stroke"></div>
      <h1 class="front-brand">Bright Fern<br>Painting</h1>
      <ul class="service-list">
        <li>Exterior Painting</li>
        <li>Interior Painting</li>
        <li>Carpentry</li>
        <li>Drywall</li>
      </ul>
    </section>

    <section class="card card-back">
      <div class="back-brand">
        <span class="brand-square"></span>
        <span>Bright Fern<br>Painting</span>
      </div>
      <div class="contact">
        <p class="person-name">MARK ELLISON</p>
        <p class="person-role">QUALITY MANAGER</p>
        <p class="contact-line">
          <svg viewBox="0 0 24 24" aria-hidden="true"><path d="M6.6 10.8a15.1 15.1 0 0 0 6.6 6.6l2.2-2.2c.3-.3.7-.4 1-.2 1.1.4 2.3.6 3.6.6.6 0 1 .4 1 1V20c0 .6-.4 1-1 1A17 17 0 0 1 3 4c0-.6.4-1 1-1h3.5c.6 0 1 .4 1 1 0 1.3.2 2.5.6 3.6.1.3 0 .7-.2 1z"/></svg>
          555-013-2468
        </p>
        <p class="contact-line">
          <svg viewBox="0 0 24 24" aria-hidden="true"><path d="M2 5h20v14H2zm2 2v.5l8 5 8-5V7z"/></svg>
          mark@brightfernpainting.com
        </p>
      </div>
      <div class="web-band">www.brightfernpainting.com</div>
      <div class="band-brush" role="img" aria-label="Small paintbrush illustration at the end of the band"></div>
    </section>
  </main>
</body>
</html>
```